1. Overview of company:
Copper Fern Mobile solutions private Ltd is one of the leading innovators & providers of Value added services (VAS) and telecom solutions to the top telecom operators across the world. We are the pioneer of several telecom technologies and products with our solutions empowering over 40 telecom giant in 51 countries.

2. Product Overview:
Vocal Twist is the most innovative voice morphing mobile app that has revolutionized the concept of IVR based offerings for telecom operators across the world. It lets you talk to your friend in a voice of your choice at just the press of a button. In addition to every call, users can now speak to their friends with background sounds of their choice.

In simple words: If person A calls person B, person A can choose the voice he wants B to listen, Words and sentences remain same just the voice changes. Person A can even activate a background sound for both of them while talking.

3. Objective of the design:
The purpose of this campaign is to establish Vocal Twist as Innovative, Lively, Youthful, Fun mobile app generally used for spreading smiles via pranks. The primary objective is to persuade the audience to download and use Vocal Twist mobile app, as well as to spread and characterize this new app.

4. Product layout:
Page 1: Landing Page
- pictorial explanation, what Vocal Twist stands for

Page 2: Home Screen options
-Navigation to vocal twist
-Navigation to sound scenery

Page 3: Vocal Twist options
-Female
-Cartoon
-King
-Bunny

Page 4: Sound scenery options
-Romantic
-Airport
-Traffic
-Football
-Church
-Beach

5. Target Audience
The users of the mobile app will be teenager whose age ranges from 16-27. The demographics are not restricted to a particular country and will be present on global level.

6. Deliverable
- 4 Uncoded screen and icon for mobile app "Vocal Twist"
- Our company name is "Copper Fern" , we would like to see designs that use Black and Green, at the same time its not mandatory.
-Design should communicate what the app stands for "Changing voice of caller"

Target Market(s)

User of the mobile app will be teenagers whose age ranges from 16-27. The demographics are not restricted to a particular country and will be present on global level. It's for masses.

Industry/Entity Type

Telecommunications

Requirements
Must have
• The design should be self explanatory, what the app stands for.
• Editable format for integration purpose.
Nice to have
• Would prefer Icons and very few words.
• Professional, elegant at the same time trendy designs.

```html
<!DOCTYPE html>
<html lang="en">
<head>
<meta charset="utf-8">
<title>Vocal Twist – app screens</title>
<link rel="stylesheet" href="https://fonts.googleapis.com/css2?family=Encode+Sans+Condensed:wght@300;400;500&display=swap">
<style>
:root{
  --page:#ffffff;
  --city-top:#3a3a3a;
  --city-mid:#2b2b2b;
  --city-bottom:#1e1e1e;
  --green:#6cc04a;
  --green-bright:#8ad33f;
  --green-deep:#3bb54a;
  --dial:#1f3d1c;
  --dial-dark:#14260f;
  --ink:#111111;
  --tab:#2a2a2a;
  --white:#ffffff;
  --muted:#bdbdbd;
  --rule:rgba(255,255,255,.55);
  --accent-yellow:#d9e021;
}
*{box-sizing:border-box;margin:0;padding:0}
html,body{width:694px;height:1200px;overflow:hidden;background:var(--page)}
body{position:relative;font-family:"Encode Sans Condensed",sans-serif;color:var(--white)}
.icon-defs{position:absolute;width:0;height:0}

.screen{position:absolute;width:217px;height:385px;overflow:hidden;
  background:linear-gradient(180deg,var(--city-top),var(--city-mid) 55%,var(--city-bottom))}
.row-1{top:10px}.row-2{top:405px}.row-3{top:800px;height:388px}
.col-1{left:10px}.col-2{left:237px}.col-3{left:464px}

.status{position:absolute;top:0;left:0;right:0;height:14px;font-size:6px;display:flex;align-items:center;justify-content:space-between;padding:0 6px;color:var(--white)}
.status .time{position:absolute;left:0;right:0;text-align:center}

.wordmark{font-weight:400;color:var(--white);letter-spacing:.2px}
.app-header{position:absolute;top:22px;left:0;right:0;height:33px;display:flex;align-items:center;justify-content:center;border-bottom:1px solid var(--rule)}
.app-header .wordmark{font-size:16px}
.app-header .burger{position:absolute;left:12px;top:11px;width:13px;height:11px}
.app-header .chev{position:absolute;right:12px;top:11px;width:12px;height:11px}
.page-title{position:absolute;top:22px;left:0;right:0;height:33px;display:flex;align-items:center;justify-content:center;color:var(--green-bright);font-size:13px;border-bottom:1px solid var(--rule)}

/* landing */
.landing .wordmark{position:absolute;top:150px;left:0;right:0;text-align:center;font-size:29px}
.landing .tag-band{position:absolute;top:283px;left:0;right:0;height:55px;background:linear-gradient(90deg,var(--green-deep),var(--green));display:flex;align-items:center;justify-content:center;text-align:center;font-size:10px;line-height:12px;font-weight:300}
.landing .tag-band::before{content:"";position:absolute;top:0;left:102px;border:6px solid transparent;border-top-color:var(--city-mid)}
.landing .legal{position:absolute;top:357px;left:0;right:0;text-align:center;font-size:5px;line-height:7px;color:var(--muted)}

/* home */
.home-btn{position:absolute;left:46px;width:125px;height:125px;border-radius:50%;background:var(--ink);display:flex;align-items:center;justify-content:center}
.home-btn::before{content:"";position:absolute;inset:9px;border-radius:50%;border:3px solid var(--green)}
.home-btn svg{width:44px;height:44px;color:var(--green)}
.home-btn.voice{top:87px}.home-btn.scene{top:222px}

/* mode screens */
.tabs{position:absolute;top:56px;left:0;right:0;height:31px;display:flex;font-size:10px}
.tab{flex:1;display:flex;align-items:center;justify-content:center;background:var(--tab);color:var(--white)}
.tab.active{background:var(--ink)}
.stage{position:absolute;top:87px;left:0;right:0;height:213px;background:linear-gradient(135deg,var(--green-bright),var(--green-deep));border-bottom:3px solid var(--ink)}
.dial{position:absolute;left:46px;top:38px;width:125px;height:125px;border-radius:50%;background:var(--dial-dark);box-shadow:0 5px 0 -1px var(--accent-yellow)}
.dial::before{content:"";position:absolute;inset:9px;border-radius:50%;background:var(--dial);border:3px solid var(--white)}
.dial svg{position:absolute;left:39px;top:39px;width:47px;height:47px;color:var(--white)}
.stage-label{position:absolute;top:184px;left:0;right:0;text-align:center;font-size:10px;color:var(--ink)}
.picker{position:absolute;top:323px;left:30px;width:157px;height:32px;border-radius:16px;background:var(--ink);display:flex;align-items:center;justify-content:center;color:#8a8a8a;font-size:13px}
.picker .chip{position:absolute;top:4px;width:24px;height:24px;border-radius:50%;background:var(--green-bright);display:flex;align-items:center;justify-content:center}
.picker .chip.left{left:4px}.picker .chip.right{right:4px}
.picker .chip svg{width:13px;height:13px;color:var(--ink)}

/* option grids */
.stage-edge{position:absolute;top:56px;left:0;width:20px;height:244px;background:var(--green-deep)}
.grid-lines{position:absolute;inset:0;width:217px;height:385px}
.option{position:absolute;width:98px;height:120px;display:flex;flex-direction:column;align-items:center;justify-content:center;gap:14px;font-size:9px;color:var(--muted)}
.option svg{width:34px;height:34px;color:var(--white)}
.option .placeholder{width:26px;height:30px;border-radius:13px 13px 6px 6px;background:var(--white)}
.o1{left:21px;top:56px}.o2{left:119px;top:56px}.o3{left:21px;top:177px}.o4{left:119px;top:177px}
.back{position:absolute;left:85px;top:322px;width:46px;height:46px;border-radius:50%;border:1px solid var(--white);display:flex;align-items:center;justify-content:center}
.back svg{width:24px;height:16px;color:var(--white)}

/* side menu */
.drawer{position:absolute;top:14px;left:0;width:110px;height:184px;background:var(--ink)}
.drawer .burger{position:absolute;left:12px;top:19px;width:13px;height:11px}
.drawer .burger-cell{position:absolute;left:0;top:8px;width:37px;height:34px;background:#262626}
.menu-item{position:absolute;left:10px;display:flex;align-items:center;gap:9px;font-size:9px;color:var(--muted)}
.menu-item svg{width:12px;height:12px;color:var(--muted)}
.mi-home{top:61px}.mi-help{top:108px}.mi-about{top:155px}

/* text pages */
.copy{position:absolute;top:62px;left:16px;right:12px;font-size:9.6px;line-height:12.6px;color:var(--white);font-weight:300}
.foot-rule{position:absolute;top:300px;left:0;right:0;border-top:1px solid var(--rule)}
</style>
</head>
<body>

<svg class="icon-defs" aria-hidden="true">
  <symbol id="i-mic" viewBox="0 0 48 48"><g fill="none" stroke="currentColor" stroke-width="2.6" stroke-linecap="round"><rect x="17" y="4" width="14" height="26" rx="7"/><path d="M11 22a13 13 0 0 0 26 0M24 35v8M16 43h16"/></g></symbol>
  <symbol id="i-globe" viewBox="0 0 48 48"><g fill="none" stroke="currentColor" stroke-width="2.6"><circle cx="24" cy="24" r="19"/><ellipse cx="24" cy="24" rx="8" ry="19"/><path d="M5 24h38M8 14h32M8 34h32"/></g></symbol>
  <symbol id="i-burger" viewBox="0 0 13 11"><path d="M0 1h13M0 5.5h13M0 10h13" stroke="currentColor" stroke-width="1.2"/></symbol>
  <symbol id="i-chev" viewBox="0 0 12 11"><path d="M6 0v10M1 5l5 5 5-5" fill="none" stroke="currentColor" stroke-width="1.2"/></symbol>
  <symbol id="i-back" viewBox="0 0 24 16"><path d="M23 8H2M9 1L2 8l7 7" fill="none" stroke="currentColor" stroke-width="1.4"/></symbol>
  <symbol id="i-plane" viewBox="0 0 34 34"><path fill="currentColor" d="M15 2h4l1 11 12 7v3l-12-3v7l4 3v2l-7-2-7 2v-2l4-3v-7L2 23v-3l12-7z"/></symbol>
  <symbol id="i-heart" viewBox="0 0 34 34"><path fill="currentColor" d="M17 31C6 22 1 17 1 10a8 8 0 0 1 16-2 8 8 0 0 1 16 2c0 7-5 12-16 21z"/></symbol>
  <symbol id="i-traffic" viewBox="0 0 34 34"><rect x="11" y="2" width="12" height="30" rx="3" fill="currentColor"/><path d="M5 6h6M23 6h6M5 15h6M23 15h6M5 24h6M23 24h6" stroke="currentColor" stroke-width="2"/><g fill="#2b2b2b"><circle cx="17" cy="8" r="3"/><circle cx="17" cy="17" r="3"/><circle cx="17" cy="26" r="3"/></g></symbol>
  <symbol id="i-ball" viewBox="0 0 34 34"><circle cx="17" cy="17" r="15" fill="currentColor"/><g fill="#2b2b2b"><path d="M17 11l6 4-2 7h-8l-2-7z"/><path d="M17 2l5 3-5 3-5-3zM31 14l-2 6-4-4 2-5zM3 14l4-3 2 5-4 4zM9 29l2-5h5l1 6zM25 29l-8 1 1-6h5z"/></g></symbol>
  <symbol id="i-crown" viewBox="0 0 34 34"><path fill="currentColor" d="M3 10l7 6 7-10 7 10 7-6-3 16H6zM6 28h22v3H6z"/></symbol>
  <symbol id="i-eyes" viewBox="0 0 34 34"><g fill="currentColor"><circle cx="9" cy="17" r="8"/><circle cx="25" cy="17" r="8"/></g><g fill="#2b2b2b"><circle cx="10" cy="17" r="4"/><circle cx="26" cy="17" r="4"/></g></symbol>
  <symbol id="i-list" viewBox="0 0 13 13"><path d="M1 3h11M1 6.5h11M1 10h11" stroke="currentColor" stroke-width="1.6"/></symbol>
  <symbol id="i-dot" viewBox="0 0 13 13"><circle cx="6.5" cy="6.5" r="5" fill="currentColor"/></symbol>
  <symbol id="i-home" viewBox="0 0 12 12"><path d="M1 6l5-5 5 5M2.5 5v6h7V5" fill="none" stroke="currentColor"/></symbol>
  <symbol id="i-help" viewBox="0 0 12 12"><circle cx="6" cy="6" r="5" fill="none" stroke="currentColor"/><path d="M4.5 4.5a1.5 1.5 0 1 1 1.5 1.6V7.5M6 9v.5" fill="none" stroke="currentColor"/></symbol>
  <symbol id="i-about" viewBox="0 0 12 12"><circle cx="6" cy="6" r="5" fill="none" stroke="currentColor"/><path d="M2 6h2l1-2 2 4 1-2h2" fill="none" stroke="currentColor"/></symbol>
</svg>

<!-- Landing -->
<section class="screen landing row-1 col-1" role="img" aria-label="Landing screen over a dim city skyline backdrop">
  <div class="status"><span>●●●●● Carrier</span><span class="time">16:05</span><span>67%</span></div>
  <div class="wordmark">vocal twist</div>
  <div class="tag-band">call &amp; change your contact voice<br>with background sound</div>
  <p class="legal">© 2015, Copper Fern Mobile solutions private Ltd.<br>All right reserved.</p>
</section>

<!-- Home -->
<section class="screen row-1 col-2" role="img" aria-label="Home screen over a dim city skyline backdrop">
  <div class="status"><span>●●●●● Carrier</span><span class="time">16:05</span><span>67%</span></div>
  <header class="app-header"><span class="wordmark">vocal twist</span></header>
  <div class="home-btn voice"><svg><use href="#i-mic"/></svg></div>
  <div class="home-btn scene"><svg><use href="#i-globe"/></svg></div>
</section>

<!-- Voice changer -->
<section class="screen row-1 col-3" role="img" aria-label="Voice changer screen over a dim city skyline backdrop">
  <div class="status"><span>●●●●● Carrier</span><span class="time">16:05</span><span>67%</span></div>
  <header class="app-header"><svg class="burger"><use href="#i-burger"/></svg><span class="wordmark">vocal twist</span><svg class="chev"><use href="#i-chev"/></svg></header>
  <nav class="tabs"><span class="tab active">Voice changer</span><span class="tab">Background sound</span></nav>
  <div class="stage"><div class="dial"><svg><use href="#i-mic"/></svg></div><p class="stage-label">Voice changer</p></div>
  <div class="picker"><span class="chip left"><svg><use href="#i-dot"/></svg></span>Bunny<span class="chip right"><svg><use href="#i-list"/></svg></span></div>
</section>

<!-- Voice options -->
<section class="screen row-2 col-1" role="img" aria-label="Voice options screen over a dim city skyline backdrop">
  <div class="status"><span>●●●●● Carrier</span><span class="time">16:05</span><span>67%</span></div>
  <div class="stage-edge"></div>
  <svg class="grid-lines"><g stroke="rgba(255,255,255,.55)" stroke-width="1"><path d="M20.5 0V385M20 55.5H217M119.5 55V297M20 176.5H217M20 297.5H217"/></g></svg>
  <div class="page-title" style="left:20px;border:0">VOICE</div>
  <div class="option o1"><span class="placeholder" role="img" aria-label="Female voice symbol"></span>Female</div>
  <div class="option o2"><svg><use href="#i-eyes"/></svg>Cartoon</div>
  <div class="option o3"><svg><use href="#i-crown"/></svg>King</div>
  <div class="option o4"><span class="placeholder" role="img" aria-label="Bunny voice symbol"></span>Bunny</div>
  <div class="back"><svg><use href="#i-back"/></svg></div>
</section>

<!-- Background sound -->
<section class="screen row-2 col-2" role="img" aria-label="Background sound screen over a dim city skyline backdrop">
  <div class="status"><span>●●●●● Carrier</span><span class="time">16:05</span><span>67%</span></div>
  <header class="app-header"><svg class="burger"><use href="#i-burger"/></svg><span class="wordmark">vocal twist</span><svg class="chev"><use href="#i-chev"/></svg></header>
  <nav class="tabs"><span class="tab">Voice changer</span><span class="tab active">Background sound</span></nav>
  <div class="stage"><div class="dial"><svg><use href="#i-globe"/></svg></div><p class="stage-label">Background sound</p></div>
  <div class="picker"><span class="chip left"><svg><use href="#i-plane"/></svg></span>Airport<span class="chip right"><svg><use href="#i-list"/></svg></span></div>
</section>

<!-- Backsound options -->
<section class="screen row-2 col-3" role="img" aria-label="Background sound options over a dim city skyline backdrop">
  <div class="status"><span>●●●●● Carrier</span><span class="time">16:05</span><span>67%</span></div>
  <div class="stage-edge"></div>
  <svg class="grid-lines"><g stroke="rgba(255,255,255,.55)" stroke-width="1"><path d="M20.5 0V385M20 55.5H217M119.5 55V297M20 176.5H217M20 297.5H217"/></g></svg>
  <div class="page-title" style="left:20px;border:0">BACKSOUND</div>
  <div class="option o1"><svg><use href="#i-plane"/></svg>Airport</div>
  <div class="option o2"><svg><use href="#i-heart"/></svg>Romantic</div>
  <div class="option o3"><svg><use href="#i-traffic"/></svg>Traffic</div>
  <div class="option o4"><svg><use href="#i-ball"/></svg>Football</div>
  <div class="back"><svg><use href="#i-back"/></svg></div>
</section>

<!-- Side menu open -->
<section class="screen row-3 col-1" role="img" aria-label="Voice changer screen with side menu open over a dim city skyline backdrop">
  <div class="status"><span>●●●●● Carrier</span><span class="time">16:05</span><span>67%</span></div>
  <header class="app-header"><span class="wordmark">vocal twist</span><svg class="chev"><use href="#i-chev"/></svg></header>
  <nav class="tabs"><span class="tab active">Voice changer</span><span class="tab">Background sound</span></nav>
  <div class="stage"><div class="dial"><svg><use href="#i-mic"/></svg></div><p class="stage-label">Voice changer</p></div>
  <div class="picker"><span class="chip left"><svg><use href="#i-dot"/></svg></span>Bunny<span class="chip right"><svg><use href="#i-list"/></svg></span></div>
  <aside class="drawer">
    <span class="burger-cell"></span><svg class="burger"><use href="#i-burger"/></svg>
    <div class="menu-item mi-home"><svg><use href="#i-home"/></svg>Home</div>
    <div class="menu-item mi-help"><svg><use href="#i-help"/></svg>Help</div>
    <div class="menu-item mi-about"><svg><use href="#i-about"/></svg>About</div>
  </aside>
</section>

<!-- About -->
<section class="screen row-3 col-2" role="img" aria-label="About page over a dim city skyline backdrop">
  <div class="status"><span>●●●●● Carrier</span><span class="time">16:05</span><span>67%</span></div>
  <div class="page-title">ABOUT</div>
  <p class="copy">Lorem ipsum dolor sit amet, consectetuer adipiscing elit, sed diam nonummy nibh euismod tincidunt ut laoreet dolore magna aliquam erat volutpat. Ut wisi enim ad minim veniam, quis nostrud exerci tation ullamcorper suscipit lobortis nisl ut aliquip ex ea commodo consequat. Duis autem vel eum iriure dolor in hendrerit in vulputate velit esse molestie consequat, vel illum dolore eu feugiat nulla facilisis at vero eros et accumsan et iusto odio dignissim qui blandit praesent luptatum zzril delenit augue duis dolore te feugait nulla facilisi. Nam liber tempor cum soluta nobis eleifend option congue nihil imperdiet doming id quod mazim placerat facer possim assum. Typi non habent</p>
  <div class="foot-rule"></div>
  <div class="back"><svg><use href="#i-back"/></svg></div>
</section>

<!-- Help -->
<section class="screen row-3 col-3" role="img" aria-label="Help page over a dim city skyline backdrop">
  <div class="status"><span>●●●●● Carrier</span><span class="time">16:05</span><span>67%</span></div>
  <div class="page-title">HELP</div>
  <p class="copy">Lorem ipsum dolor sit amet, consectetuer adipiscing elit, sed diam nonummy nibh euismod tincidunt ut laoreet dolore magna aliquam erat volutpat. Ut wisi enim ad minim veniam, quis nostrud exerci tation ullamcorper suscipit lobortis nisl ut aliquip ex ea commodo consequat. Duis autem vel eum iriure dolor in hendrerit in vulputate velit esse molestie consequat, vel illum dolore eu feugiat nulla facilisis at vero eros et accumsan et iusto odio dignissim qui blandit praesent luptatum zzril delenit augue duis dolore te feugait nulla facilisi. Nam liber tempor cum soluta nobis eleifend option congue nihil imperdiet doming id quod mazim placerat facer possim assum. Typi non habent</p>
  <div class="foot-rule"></div>
  <div class="back"><svg><use href="#i-back"/></svg></div>
</section>

</body>
</html>
```